Box Design of "pet rapid test for dogs & cats" with professional use

"The market is in Southeast Asia, South America, Europe, and the U.S."
Clients: Veterinary clinics, pet hospitals,(a small number of home use)

Primary colors:
Orange, Green,or Blue, (select 1,or 2 color)
Neutrals: Black, Gray, or White (optional)
Dimensions:135mm(L)*90mm(W)*105mm(W)

Kindly review the attached file for additional content
Updates

I have increased my budget, please provide a satisfactory design solution, thank you very much for your work.

Target Market(s)

Southeast Asia, South America, Europe, and the U.S.

Industry/Entity Type

Veterinary test kit for dogs & cats

Colors
0054AA
0677BA
7BADD7
CADEEF
E8F1F8
0094D4
00A9DD
6FCCEA
C7EBF8
E9F6FB
00AB8E
00BBA5
67D7C9
C6EFE9
E9F9F6
59FF00
82FF00
B8FF75
E3FFCB
F4FFEA
F0912C
F2A743
F7CA91
FBE8D2
FDF5EE
EE7325
F08F49
F5BC92
FAE3D3
FDF4ED

Requirements
Nice to have
• Appealing Box Appearance with professional

```html
<!DOCTYPE html>
<html lang="en">
<head>
<meta charset="utf-8">
<title>VETLUMA Pet Rapid Test Kit – Box Dieline</title>
<link href="https://fonts.googleapis.com/css2?family=Roboto:ital,wght@0,300;0,400;0,500;0,700;1,300&display=swap" rel="stylesheet">
<style>
  :root{
    --navy:#0a4369;
    --white:#ffffff;
    --paw:#dce5ee;
    --cut:#d9336c;
    --soft:#c9d9e6;
  }
  *{margin:0;padding:0;box-sizing:border-box}
  html,body{width:1200px;height:900px;overflow:hidden;background:var(--white)}
  body{font-family:"Roboto",sans-serif;color:var(--navy);position:relative}
  .abs{position:absolute}
  .panel{position:absolute}
  .panel--navy{background:var(--navy);color:var(--white)}
  .dieline{position:absolute;left:0;top:0;width:1200px;height:900px;pointer-events:none}
  .brand{position:absolute;font-weight:500;letter-spacing:.2px;white-space:nowrap;line-height:1}
  .brand-mark{position:absolute;border:2px solid currentColor;border-radius:50%}
  .paw-area{position:absolute;background:var(--paw);border-radius:0 0 0 40px}
  .ribbon{position:absolute;background:var(--navy);color:var(--white);font-weight:700;font-size:10px;line-height:12px;padding:5px 0 0 19px;clip-path:polygon(10px 0,100% 0,100% 100%,0 100%)}
  .contents-title{position:absolute;font-weight:700;font-size:11.5px;color:#111}
  .contents-list{position:absolute;list-style:none;font-size:8.4px;color:#222}
  .contents-list li{height:17.4px}
  .count-badge{position:absolute;width:57px;height:57px;border-radius:50%;background:var(--navy);box-shadow:0 0 0 1.5px var(--white) inset,0 0 0 3px var(--navy) inset;color:var(--white);text-align:center}
  .count-badge .num{position:absolute;left:0;right:0;top:6px;font-size:20px;font-style:italic;font-weight:500;transform:rotate(8deg)}
  .count-badge .unit{position:absolute;left:0;right:0;top:26px;font-size:8.5px;font-weight:500;transform:rotate(14deg);line-height:9px}
  .icons{position:absolute;display:flex;gap:13px;align-items:center}
  .icons svg{display:block}
  .storage{position:absolute;text-align:center;font-size:9px;line-height:11.5px;color:var(--navy)}
  .tagline-band{position:absolute;background:var(--navy);color:var(--white);text-align:center;font-size:12px;letter-spacing:.2px;line-height:27px}
  .sticker-box{position:absolute;border:1.2px solid var(--soft);border-radius:8px;display:flex;align-items:center;justify-content:center;font-size:11.5px;letter-spacing:.3px}
  .maker{position:absolute;text-align:center;font-style:italic;font-weight:300;font-size:8.5px;color:#c5d6e4}
  .side-tag{position:absolute;text-align:center;font-size:10px;letter-spacing:.2px}
  .features{position:absolute;font-size:4.4px;line-height:5.2px;color:var(--white)}
  .features dt{font-weight:700;margin-top:2.4px}
  .features dd{font-weight:400}
</style>
</head>
<body>

<!-- Lid panel -->
<section class="panel panel--navy lid" style="left:31px;top:119px;width:342px;height:266px">
  <span class="brand-mark" style="left:145px;top:92px;width:44px;height:44px"></span>
  <span class="brand" style="left:0;right:0;top:152px;text-align:center;font-size:25px">VETLUMA™</span>
</section>

<!-- Front panel (English) -->
<section class="panel front-en" style="left:31px;top:385px;width:342px;height:266px">
  <div class="paw-area" role="img" aria-label="Soft pale paw-print pattern" style="left:224px;top:0;width:118px;height:60px"></div>
  <span class="brand-mark" style="left:57px;top:24px;width:44px;height:44px;color:var(--navy)"></span>
  <span class="brand" style="left:20px;top:77px;font-size:22px">VETLUMA™</span>
  <div class="ribbon" style="left:156px;top:61px;width:186px;height:34px">PET RAPID TEST KIT for<br>Dogs &amp; Cats</div>
  <div class="contents-title" style="left:41px;top:114px">CONTENTS:</div>
  <ol class="contents-list" style="left:21px;top:136px">
    <li>1.&nbsp; Test Kits(Cassett, disposable dropper,desiccant).</li>
    <li>2.&nbsp; Assay buffer.</li>
    <li>3.&nbsp; Sterile swabs.</li>
    <li>4.&nbsp; Instruction manual.</li>
  </ol>
  <div class="count-badge" style="left:253px;top:140px"><span class="num">10</span><span class="unit">Tests/box</span></div>
  <div class="icons" style="left:41px;top:215px">
    <svg width="20" height="12" viewBox="0 0 20 12"><rect x=".6" y=".6" width="18.8" height="10.8" fill="none" stroke="#0a4369" stroke-width="1"/><text x="10" y="9" font-size="7.5" font-weight="700" text-anchor="middle" fill="#0a4369" font-family="Roboto,sans-serif">IVD</text></svg>
    <svg width="14" height="18" viewBox="0 0 14 18"><path d="M7 1V17M3 12H11M3 12V15M11 3H13" stroke="#0a4369" stroke-width="1.2" fill="none"/></svg>
    <svg width="14" height="18" viewBox="0 0 14 18"><path d="M7 1V9M3 3L11 9M11 3L3 9M1 6H13" stroke="#0a4369" stroke-width="1"/><rect x="4" y="11" width="6" height="6" fill="#0a4369"/></svg>
    <svg width="22" height="16" viewBox="0 0 22 16"><path d="M1 2L11 1V15L1 15ZM11 1L21 2V15L11 15" fill="none" stroke="#0a4369" stroke-width="1"/><text x="16" y="12" font-size="9" font-weight="700" text-anchor="middle" fill="#0a4369" font-family="Roboto,sans-serif">i</text></svg>
    <svg width="20" height="20" viewBox="0 0 20 20"><circle cx="10" cy="10" r="8.8" fill="none" stroke="#0a4369" stroke-width="1.2"/><path d="M4 4L16 16M6 15C8 10 12 10 14 15M10 5A2.5 2.5 0 1 1 10 10" fill="none" stroke="#0a4369" stroke-width="1.1"/></svg>
  </div>
  <div class="storage" style="left:222px;top:208px;width:104px">Store at 2~30°C<br>Avoid direct sunlight</div>
  <div class="tagline-band" style="left:0;top:239px;width:342px;height:27px">LOVED BY PETS, TRUSTED BY VETS</div>
</section>

<!-- Side panel (sticker) -->
<section class="panel panel--navy side-label" style="left:373px;top:385px;width:228px;height:266px">
  <span class="brand-mark" style="left:95px;top:8px;width:36px;height:36px"></span>
  <span class="brand" style="left:0;right:0;top:53px;text-align:center;font-size:18px">VETLUMA™</span>
  <div class="sticker-box" style="left:24px;top:94px;width:178px;height:123px">STICKER / LABEL</div>
  <div class="maker" style="left:0;right:0;top:236px">MADE by NORAVET™</div>
  <div class="side-tag" style="left:0;right:0;top:250px">LOVED BY PETS, TRUSTED BY VETS</div>
</section>

<!-- Front panel (Spanish) -->
<section class="panel front-es" style="left:601px;top:385px;width:341px;height:266px">
  <div class="paw-area" role="img" aria-label="Soft pale paw-print pattern" style="left:223px;top:0;width:118px;height:60px"></div>
  <span class="brand-mark" style="left:57px;top:24px;width:44px;height:44px;color:var(--navy)"></span>
  <span class="brand" style="left:20px;top:77px;font-size:22px">VETLUMA™</span>
  <div class="ribbon" style="left:155px;top:61px;width:186px;height:34px;font-size:9.6px;padding-left:12px">KIT DE PRUEBA RÁPIDA<br>PARA MASCOTAS (Perros y Gatos)</div>
  <div class="contents-title" style="left:38px;top:114px">CONTENIDO:</div>
  <ol class="contents-list" style="left:20px;top:136px">
    <li>1.&nbsp; Kits de prueba (cassette, gotero desechable, desecante).</li>
    <li>2.&nbsp; Buffer de ensayo.</li>
    <li>3.&nbsp; Hisopos estériles.</li>
    <li>4.&nbsp; Manual de instrucciones.</li>
  </ol>
  <div class="count-badge" style="left:263px;top:140px"><span class="num">10</span><span class="unit">pruebas<br>por caja</span></div>
  <div class="icons" style="left:30px;top:215px">
    <svg width="20" height="12" viewBox="0 0 20 12"><rect x=".6" y=".6" width="18.8" height="10.8" fill="none" stroke="#0a4369" stroke-width="1"/><text x="10" y="9" font-size="7.5" font-weight="700" text-anchor="middle" fill="#0a4369" font-family="Roboto,sans-serif">IVD</text></svg>
    <svg width="14" height="18" viewBox="0 0 14 18"><path d="M7 1V17M3 12H11M3 12V15M11 3H13" stroke="#0a4369" stroke-width="1.2" fill="none"/></svg>
    <svg width="14" height="18" viewBox="0 0 14 18"><path d="M7 1V9M3 3L11 9M11 3L3 9M1 6H13" stroke="#0a4369" stroke-width="1"/><rect x="4" y="11" width="6" height="6" fill="#0a4369"/></svg>
    <svg width="22" height="16" viewBox="0 0 22 16"><path d="M1 2L11 1V15L1 15ZM11 1L21 2V15L11 15" fill="none" stroke="#0a4369" stroke-width="1"/><text x="16" y="12" font-size="9" font-weight="700" text-anchor="middle" fill="#0a4369" font-family="Roboto,sans-serif">i</text></svg>
    <svg width="20" height="20" viewBox="0 0 20 20"><circle cx="10" cy="10" r="8.8" fill="none" stroke="#0a4369" stroke-width="1.2"/><path d="M4 4L16 16M6 15C8 10 12 10 14 15M10 5A2.5 2.5 0 1 1 10 10" fill="none" stroke="#0a4369" stroke-width="1.1"/></svg>
  </div>
  <div class="storage" style="left:200px;top:211px;width:116px">Almacenamiento 2~30°C<br>Evitar la luz solar directa</div>
  <div class="tagline-band" style="left:0;top:239px;width:341px;height:27px;font-size:11px">QUERIDO POR LAS MASCOTAS, CONFIADO POR VETERINARIOS</div>
</section>

<!-- Side panel (features) -->
<section class="panel panel--navy side-features" style="left:942px;top:385px;width:228px;height:266px">
  <span class="brand-mark" style="left:95px;top:8px;width:36px;height:36px"></span>
  <span class="brand" style="left:0;right:0;top:53px;text-align:center;font-size:18px">VETLUMA™</span>
  <dl class="features" style="left:16px;top:80px;width:200px">
    <dt>SIMPLE &amp; CONVENIENT:</dt><dd>no professional skills required, Simple enough for home use.</dd>
    <dt>FÁCIL Y PRÁCTICO:</dt><dd>Sin capacitación previa, Suficientemente simple para uso en casa.</dd>
    <dt>FAST &amp; EFFICIENT:</dt><dd>Digital results in &lt; 10 minutes - from start to completion.</dd>
    <dt>RÁPIDO Y EFICIENTE:</dt><dd>Resultados digitales en &lt;10 minutos, Desde inicio hasta resultado final.</dd>
    <dt>ACCURATE &amp; RELIABLE:</dt><dd>Quick and trustworthy pet health results using advanced lateral flow biotech, Trusted by vet clinics worldwide.</dd>
    <dt>PRECISO Y FIABLE:</dt><dd>Resultados rápidos y confiables con tecnología de inmunocromatografía avanzada, Validado por clínicas veterinarias a nivel global.</dd>
    <dt>MULTI-DISEASE DETECTION:</dt><dd>Supports screening of multiple diseases, Helping pet owners detect issues early.</dd>
    <dt>DETECCIÓN MULTIENFERMEDADES:</dt><dd>Resultados rápidos y confiables con tecnología de inmunocromatografía avanzada, Validado por clínicas veterinarias a nivel global.</dd>
  </dl>
  <div class="maker" style="left:0;right:0;top:236px">MADE by NORAVET™</div>
  <div class="side-tag" style="left:0;right:0;top:250px">LOVED BY PETS, TRUSTED BY VETS</div>
</section>

<!-- Cut lines -->
<svg class="dieline" viewBox="0 0 1200 900" fill="none" stroke="#d9336c" stroke-width="1">
  <path d="M32 119V108Q32 82 62 82H342Q372 82 372 108V119"/>
  <path d="M31 119H373V651H31Z"/>
  <path d="M373 385H1170V651H373M601 385V651M942 385V651"/>
  <path d="M373 385L377 380V283H565Q593 283 593 311V370L601 376V385"/>
  <path d="M942 385L947 379V283H1134Q1162 283 1162 311V370L1170 376V651"/>
  <path d="M31 651V817H95Q107 817 107 805V767H298V805Q298 817 310 817H373V651"/>
  <path d="M373 651L486 728V764Q486 780 502 780H601V651"/>
  <path d="M601 651L677 765V801Q677 814 690 814H855Q867 814 867 801V763L942 651"/>
  <path d="M942 651L1056 729V764Q1056 780 1072 780H1170V651"/>
</svg>

</body>
</html>
```